Dog Food Bag Packaging Redesign

Hey there..We're a small dog food company, focusing on all natural, locally sourced, high quality ingredients. They're patties, and baked for 10 min. Dogs go insane for them. We're looking to redo our packaging, and thus, its design. I've attached images. Currently, we are wrapping 12 patties in a poly bag and then butcher paper, and sticking a label on it. We're moving to a zipper seal poly that's black. I've attached the design concept from our bag manufacturer for your reference only. We don't necessarily want to use our old label, but we're not against using elements of it. We really like our current label.. I'm just not so sure it's the right call for a poly bag.We have three flavours; chicken, beef, lamb. I would LOVE to know what flavour the bag is without having to be super close to the bag. So perhaps the top part (1-4 inches) could be the flavour colour? I will have to provide some verbiage for the back. I need to add feeding instructions, and a bit of a thank you story. I'm open for suggestions on how to display ingredients/nutritional facts.

Target Market(s)

Dog Owners

Industry/Entity Type

Manufacturing

Font styles to use
Sans Serif

Colors
9bcb3c

Requirements
Must have
• Total bag design. When you submit your design, please submit your designs on top of a bag. It makes it much easier to visual the end product.
• The bag needs to have the associated flavour colours on it to differentiate flavour from a distance. Red = beef, yellow = chicken, purple = lamb.
• I'm happy with the logo being on the back only, but if on the front it needs to be small. Patties should be the main header word.
Nice to have
• I like the idea of a vertical colour bar on the side of the bag to show its flavour, but I'm not again a top horizontal bar either.
• I like PATTIES being the biggest word on the bag.

```html
<!DOCTYPE html>
<html lang="en">
<head>
<meta charset="utf-8">
<title>Patties Bag Labels</title>
<link href="https://fonts.googleapis.com/css2?family=Fredoka:wght@600&family=Oswald:wght@400;500&display=swap" rel="stylesheet">
<style>
  :root {
    --chicken: #f7a823;
    --beef: #d4262f;
    --lamb: #b0378f;
    --ink: #1d1a1b;
    --paper: #ffffff;
    --body: #f3f3f3;
    --accent-text: #b0378f;
    --dog-light: #c98a4e;
    --dog-dark: #6b4526;
  }
  * { box-sizing: border-box; margin: 0; padding: 0; }
  html, body { width: 1200px; height: 931px; overflow: hidden; background: var(--paper); }
  .canvas { position: relative; width: 1200px; height: 931px; }

  .label {
    position: absolute;
    width: 11.8em;
    height: 24.4em;
    background: var(--paper);
    display: flex;
    flex-direction: column;
    overflow: hidden;
  }
  .label--small { font-size: 10px; }
  .label--large { font-size: 18.7px; box-shadow: 0 0.2em 0.6em rgba(0,0,0,0.12); }

  .label--chicken { --flavour: var(--chicken); }
  .label--beef { --flavour: var(--beef); }
  .label--lamb { --flavour: var(--lamb); }

  .flavour-band {
    height: 5.4em;
    background: var(--flavour);
    display: flex;
    align-items: flex-end;
    justify-content: center;
    padding-bottom: 0.6em;
  }
  .flavour-band__note {
    font-family: 'Oswald', sans-serif;
    font-size: 0.55em;
    letter-spacing: 0.35em;
    color: rgba(255,255,255,0.85);
  }
  .flavour-name {
    font-family: 'Fredoka', sans-serif;
    font-weight: 600;
    font-size: 2.2em;
    line-height: 1.4;
    text-align: center;
    color: var(--flavour);
    letter-spacing: 0.02em;
    white-space: nowrap;
  }
  .label-body {
    flex: 1;
    background: linear-gradient(180deg, var(--body), var(--paper));
    display: flex;
    flex-direction: column;
    align-items: center;
    padding-top: 0.8em;
  }
  .patties-tag {
    font-family: 'Fredoka', sans-serif;
    font-weight: 600;
    font-size: 1.3em;
    line-height: 1.2;
    color: var(--paper);
    background: var(--flavour);
    padding: 0 0.3em;
    letter-spacing: 0.03em;
  }
  .brand {
    margin-top: 0.9em;
    display: flex;
    align-items: center;
    gap: 0.25em;
  }
  .brand__dot { width: 0.7em; height: 0.7em; border-radius: 50%; background: var(--ink); }
  .brand__name {
    font-family: 'Oswald', sans-serif;
    font-weight: 500;
    font-size: 0.55em;
    color: var(--ink);
    letter-spacing: 0.05em;
  }
  .stars { font-size: 0.45em; letter-spacing: 0.35em; color: var(--ink); margin-top: 0.2em; }
  .ingredients {
    margin-top: 1.1em;
    font-family: 'Oswald', sans-serif;
    font-size: 0.58em;
    line-height: 1.3;
    text-align: center;
    color: var(--ink);
    padding: 0 0.8em;
  }
  .pack-size {
    align-self: flex-end;
    margin-right: 1.4em;
    font-family: 'Oswald', sans-serif;
    font-size: 0.45em;
    line-height: 1.15;
    text-align: right;
    color: var(--accent-text);
  }
  .dog-photo {
    margin-top: auto;
    width: 100%;
    height: 5.2em;
    background: radial-gradient(ellipse 48% 100% at 50% 100%, var(--dog-light) 0%, var(--dog-dark) 65%, rgba(255,255,255,0) 100%);
  }
  .tagline-band {
    height: 2.9em;
    background: var(--ink);
    display: flex;
    align-items: center;
    justify-content: center;
  }
  .tagline-band__text {
    font-family: 'Oswald', sans-serif;
    font-size: 0.58em;
    letter-spacing: 0.08em;
    color: var(--paper);
    white-space: nowrap;
  }
</style>
</head>
<body>
<main class="canvas">

  <article class="label label--small label--chicken" style="left:364px; top:50px;">
    <div class="flavour-band"><span class="flavour-band__note">deboned</span></div>
    <h2 class="flavour-name">CHICKEN</h2>
    <div class="label-body">
      <span class="patties-tag">PATTIES</span>
      <div class="brand"><span class="brand__dot"></span><span class="brand__name">PAWSTEAD</span></div>
      <div class="stars">★★★★★</div>
      <p class="ingredients">deboned chicken, fresh eggs, apples,<br>fresh potatoes, broccoli, carrots</p>
      <p class="pack-size">12 PATTIES<br>3 LB</p>
      <div class="dog-photo" role="img" aria-label="Photo of a dog peeking up over the label edge"></div>
    </div>
    <div class="tagline-band"><span class="tagline-band__text">fresh · local · responsible</span></div>
  </article>

  <article class="label label--small label--beef" style="left:529px; top:50px;">
    <div class="flavour-band"><span class="flavour-band__note">grass-fed</span></div>
    <h2 class="flavour-name">BEEF</h2>
    <div class="label-body">
      <span class="patties-tag">PATTIES</span>
      <div class="brand"><span class="brand__dot"></span><span class="brand__name">PAWSTEAD</span></div>
      <div class="stars">★★★★★</div>
      <p class="ingredients">grass-fed beef, fresh eggs, apples,<br>fresh potatoes, broccoli, carrots</p>
      <p class="pack-size">12 PATTIES<br>3 LB</p>
      <div class="dog-photo" role="img" aria-label="Photo of a dog peeking up over the label edge"></div>
    </div>
    <div class="tagline-band"><span class="tagline-band__text">fresh · local · responsible</span></div>
  </article>

  <article class="label label--small label--lamb" style="left:690px; top:50px;">
    <div class="flavour-band"><span class="flavour-band__note">deboned</span></div>
    <h2 class="flavour-name">LAMB</h2>
    <div class="label-body">
      <span class="patties-tag">PATTIES</span>
      <div class="brand"><span class="brand__dot"></span><span class="brand__name">PAWSTEAD</span></div>
      <div class="stars">★★★★★</div>
      <p class="ingredients">deboned lamb, fresh eggs, apples,<br>fresh potatoes, broccoli, carrots</p>
      <p class="pack-size">12 PATTIES<br>3 LB</p>
      <div class="dog-photo" role="img" aria-label="Photo of a dog peeking up over the label edge"></div>
    </div>
    <div class="tagline-band"><span class="tagline-band__text">fresh · local · responsible</span></div>
  </article>

  <article class="label label--large label--chicken" style="left:101px; top:462px;">
    <div class="flavour-band"><span class="flavour-band__note">deboned</span></div>
    <h2 class="flavour-name">CHICKEN</h2>
    <div class="label-body">
      <span class="patties-tag">PATTIES</span>
      <div class="brand"><span class="brand__dot"></span><span class="brand__name">PAWSTEAD</span></div>
      <div class="stars">★★★★★</div>
      <p class="ingredients">deboned chicken, fresh eggs, apples,<br>fresh potatoes, broccoli, carrots</p>
      <p class="pack-size">12 PATTIES<br>3 LB</p>
      <div class="dog-photo" role="img" aria-label="Photo of a dog peeking up over the label edge"></div>
    </div>
    <div class="tagline-band"><span class="tagline-band__text">fresh · local · responsible</span></div>
  </article>

  <article class="label label--large label--beef" style="left:484px; top:462px;">
    <div class="flavour-band"><span class="flavour-band__note">grass-fed</span></div>
    <h2 class="flavour-name">BEEF</h2>
    <div class="label-body">
      <span class="patties-tag">PATTIES</span>
      <div class="brand"><span class="brand__dot"></span><span class="brand__name">PAWSTEAD</span></div>
      <div class="stars">★★★★★</div>
      <p class="ingredients">grass-fed beef, fresh eggs, apples,<br>fresh potatoes, broccoli, carrots</p>
      <p class="pack-size">12 PATTIES<br>3 LB</p>
      <div class="dog-photo" role="img" aria-label="Photo of a dog peeking up over the label edge"></div>
    </div>
    <div class="tagline-band"><span class="tagline-band__text">fresh · local · responsible</span></div>
  </article>

  <article class="label label--large label--lamb" style="left:856px; top:462px;">
    <div class="flavour-band"><span class="flavour-band__note">deboned</span></div>
    <h2 class="flavour-name">LAMB</h2>
    <div class="label-body">
      <span class="patties-tag">PATTIES</span>
      <div class="brand"><span class="brand__dot"></span><span class="brand__name">PAWSTEAD</span></div>
      <div class="stars">★★★★★</div>
      <p class="ingredients">deboned lamb, fresh eggs, apples,<br>fresh potatoes, broccoli, carrots</p>
      <p class="pack-size">12 PATTIES<br>3 LB</p>
      <div class="dog-photo" role="img" aria-label="Photo of a dog peeking up over the label edge"></div>
    </div>
    <div class="tagline-band"><span class="tagline-band__text">fresh · local · responsible</span></div>
  </article>

</main>
</body>
</html>
```